Private Chef booking platform landing page design

I need an amazing design for a landing page for my upcoming private chef booking platform Platerva. You can view my current page here: www.platerva.co.uk/mainindex.php. The design on this page is wrong right now. This platform is in Beta and the main purpose is to sign up chefs. Similar to what Rydexa.com is doing with their website -> become a driver. In my case we should have a button that says "become a chef", state the benefits of becoming a chef such as earning extra money, managing your time and bookings, increasing your client base and be creative with your food menus at the same time. Also, somewhere on the website it needs to say that we are currently in Beta mode and sign up to help us grow. In terms of visuals, I want the design to be sleek and clean and also adaptable to mobile devices as I am using html5. You can also re-design the current logo and choose any colours you think would be suitable for such a concept. Similar concept websites: hobwanderly.com and stovlin.com
Updates

Target Market(s)

upper middle class

Industry/Entity Type

Chef

Number of Pages Required

1 page

Font styles to use
Sans Serif

Requirements
Must have
• see brief and check hobwanderly.com and stovlin.com for inspiration and also rydexa.com
Nice to have
• see brief
Should not have
• bad visuals

```html
<!DOCTYPE html>
<html lang="en">
<head>
<meta charset="utf-8">
<title>Platerva – Private Chef Booking</title>
<link rel="stylesheet" href="https://fonts.googleapis.com/css2?family=Ubuntu:wght@400;500;700&display=swap">
<style>
:root{
  --dark:#262626;
  --dark-glass:rgba(38,38,38,.86);
  --header-glass:rgba(30,30,30,.72);
  --yellow:#f7b500;
  --orange:#f15a24;
  --gold-text:#e8a000;
  --cream:#fdf5e2;
  --cream-deep:#fbefd3;
  --ink:#222;
  --body:#333;
  --white:#fff;
  --social:#3b5fa8;
}
*{box-sizing:border-box;margin:0;padding:0}
html,body{width:1023px;height:1200px;overflow:hidden}
body{font-family:"Ubuntu",sans-serif;color:var(--body);background:var(--white);position:relative}
a{color:inherit;text-decoration:none}

.hero{position:absolute;left:0;top:0;width:1023px;height:428px;
  background:
    radial-gradient(ellipse 160px 110px at 560px 275px,#b9d84a 0%,rgba(185,216,74,0) 100%),
    radial-gradient(ellipse 260px 110px at 320px 260px,#c9a06a 0%,rgba(201,160,106,0) 100%),
    radial-gradient(ellipse 220px 180px at 470px 120px,#e9d8cc 0%,rgba(233,216,204,0) 100%),
    linear-gradient(180deg,#c9c9c4 0%,#a9aaa3 55%,#6f7063 100%)}

.site-header{position:absolute;left:0;top:0;width:1023px;height:44px;background:var(--header-glass)}
.brand{position:absolute;left:138px;top:11px;font-size:20px;font-weight:400;color:var(--yellow)}
.main-nav{position:absolute;left:606px;top:0;height:44px;display:flex;font-size:11px;color:var(--white)}
.main-nav a{display:block;height:44px;line-height:44px;padding:0 9px}
.main-nav .nav-signup{background:var(--yellow);color:var(--ink);margin-left:6px}
.main-nav .nav-login{background:var(--orange)}

.beta-notice{position:absolute;left:136px;top:384px;height:28px;line-height:28px;padding:0 12px;background:var(--dark-glass);color:var(--white);font-size:10.5px}
.beta-notice strong{color:var(--yellow);font-weight:500;margin-right:6px}

.login-panel{position:absolute;left:612px;top:203px;width:273px;height:225px}
.login-tabs{display:flex;height:25px;font-size:11.5px;font-weight:500}
.login-tabs span{display:block;line-height:25px;text-align:center}
.tab-client{width:132px;background:var(--dark-glass);color:var(--white)}
.tab-chef{width:141px;background:rgba(255,255,255,.55);color:var(--ink)}
.login-body{position:relative;height:200px;background:var(--dark-glass);padding:15px 12px 0}
.social-connect{display:flex;align-items:center;height:36px;background:var(--social);color:var(--white);font-size:11px}
.social-connect .mark{width:8px;height:8px;margin:0 48px 0 18px;background:var(--white)}
.or-email{color:var(--white);font-size:10px;text-align:center;margin:7px 0 6px}
.field{display:flex;align-items:center;height:34px;background:var(--white);margin-bottom:4px;font-size:10.5px;color:#777}
.field svg{margin:0 12px 0 9px}
.login-actions{display:flex;align-items:center;margin-top:6px;font-size:10.5px;color:var(--white)}
.btn-signin{display:block;width:57px;height:29px;line-height:29px;text-align:center;background:var(--yellow);color:var(--ink)}
.login-actions .forgot{margin-left:14px}

.intro{position:absolute;left:0;top:428px;width:1023px;height:193px;background:var(--cream)}
.intro .col-chef{position:absolute;left:512px;top:0;width:511px;height:193px;background:var(--cream-deep)}
.intro-block{position:absolute;top:22px;width:360px}
.intro-head{display:flex;align-items:center;justify-content:space-between;height:22px;margin-bottom:6px}
.intro-block h2{font-size:17px;font-weight:500;color:var(--ink)}
.intro-block p{font-size:10.4px;line-height:14px;color:var(--body);margin-bottom:9px}
.btn-become{display:block;height:22px;line-height:22px;padding:0 12px;background:var(--yellow);color:var(--ink);font-size:10.5px;font-weight:500}
.need{left:136px}
.am{left:536px}

.features{position:absolute;left:0;top:621px;width:1023px;height:146px;background:var(--white)}
.feature{position:absolute;top:30px;width:180px;text-align:center}
.feature svg{display:block;margin:0 auto 9px}
.feature h3{font-size:10.5px;font-weight:500;color:var(--gold-text);letter-spacing:.2px;margin-bottom:4px}
.feature p{font-size:10.4px;line-height:14px;color:var(--body)}

.city-map{position:absolute;left:0;top:767px;width:1023px;height:222px;
  background:radial-gradient(ellipse 300px 120px at 530px 120px,#f3d67a 0%,rgba(243,214,122,0) 100%),
  linear-gradient(180deg,#f0d98a 0%,#e8cf78 100%)}
.city-search{position:absolute;left:417px;top:861px;width:190px;height:34px;display:flex;border:2px solid var(--yellow);background:var(--white)}
.city-search .pin{width:32px;display:flex;align-items:center;justify-content:center}
.city-search .label{flex:1;font-size:10.5px;color:#666;line-height:30px}
.city-search .go{width:32px;background:var(--yellow);display:flex;align-items:center;justify-content:center}

.testimonials{position:absolute;left:0;top:989px;width:1023px;height:160px;text-align:center}
.testimonials h2{font-size:18px;font-weight:400;color:var(--ink);margin-top:23px;margin-bottom:10px}
.testimonials blockquote{width:760px;margin:0 auto;font-size:10.4px;line-height:14px;color:var(--body)}
.testimonials .q{font-size:15px;line-height:0}
.testimonials .who{font-size:10px;color:var(--gold-text);margin-top:7px}
.testimonials .role{font-size:10px;color:var(--ink);margin-top:3px}
.slider-dots{display:flex;justify-content:center;gap:4px;margin-top:7px}
.slider-dots span{width:15px;height:3px;background:#666}
.slider-dots .on{background:var(--yellow)}

.site-footer{position:absolute;left:0;top:1149px;width:1023px;height:51px;background:var(--dark)}
.footer-nav{position:absolute;left:137px;top:12px;display:flex;font-size:10px;color:var(--white)}
.footer-nav a{padding:0 7px;border-left:1px solid #666}
.footer-nav a:first-child{padding-left:0;border-left:0}
.copyright{position:absolute;left:137px;top:33px;font-size:8.5px;color:#999}
.social-links{position:absolute;left:811px;top:13px;display:flex;gap:3px}
.social-links span{width:15px;height:15px;display:block}
</style>
</head>
<body>

<div class="hero" role="img" aria-label="Blurred kitchen photo: hands slicing green peppers on a wooden chopping board"></div>

<header class="site-header">
  <div class="brand">Platerva</div>
  <nav class="main-nav">
    <a href="#">HOME</a>
    <a href="#">CONTACT US</a>
    <a href="#">ABOUT US</a>
    <a href="#" class="nav-signup">SIGN UP</a>
    <a href="#" class="nav-login">LOGIN</a>
  </nav>
</header>

<p class="beta-notice"><strong>BETA</strong>We are currently in Beta – sign up to help us grow.</p>

<section class="login-panel">
  <div class="login-tabs">
    <span class="tab-client">LOG IN AS A CLIENT</span>
    <span class="tab-chef">LOG IN AS A CHEF</span>
  </div>
  <div class="login-body">
    <a href="#" class="social-connect"><span class="mark"></span>CONNECT WITH FRIENDLOOP</a>
    <p class="or-email">or use email</p>
    <label class="field">
      <svg width="22" height="16" viewBox="0 0 22 16"><rect x="1" y="1" width="20" height="14" fill="none" stroke="#444" stroke-width="1.5"/><path d="M1 1l10 8 10-8" fill="none" stroke="#444" stroke-width="1.5"/></svg>
      Email Address
    </label>
    <label class="field">
      <svg width="22" height="18" viewBox="0 0 22 18"><rect x="1" y="3" width="20" height="14" fill="none" stroke="#444" stroke-width="1.5"/><rect x="5" y="1" width="12" height="3" fill="#444"/><rect x="13" y="9" width="5" height="5" fill="#444"/></svg>
      Password
    </label>
    <div class="login-actions">
      <a href="#" class="btn-signin">SIGN IN</a>
      <a href="#" class="forgot">Forgot Password</a>
    </div>
  </div>
</section>

<section class="intro">
  <div class="col-chef"></div>
  <div class="intro-block need">
    <div class="intro-head"><h2>I NEED A CHEF!</h2></div>
    <p>Lorem ipsum dolor sit amet, consectetur adipiscing elit. Ut interdum tellus mi, in condimentum odio convallis eu. Proin pellentesque arcu eu elementum viverra. In posuere elit non metus laoreet sagittis. Etiam eu nisi vehicula leo ornare luctus. Cras quis augue augue. Pellentesque sed placerat lacus. In molestie laoreet consectetur. In placerat mi a arcu molestie, vel lacinia libero dignissim.</p>
    <p>Donec sed cursus lorem. Nullam ac eleifend turpis. Donec tincidunt faucibus tortor, nec iaculis ipsum imperdiet eget.</p>
  </div>
  <div class="intro-block am">
    <div class="intro-head"><h2>I AM A CHEF!</h2><a href="#" class="btn-become">BECOME A CHEF</a></div>
    <p>Earn extra money, manage your own time and bookings, grow your client base and be creative with your menus. Curabitur vitae blandit ante.</p>
    <p>Integer vestibulum rutrum purus, ac aliquam ipsum eleifend vel. Donec et iaculis enim. Etiam luctus viverra fermentum. Donec in euismod lectus, et pretium risus. Nulla sagittis ligula enim, eget pretium dolor posuere nec. Mauris eu mauris vitae tortor congue consectetur id fringilla diam. Hunc nec interdum nulla.</p>
  </div>
</section>

<section class="features">
  <div class="feature" style="left:139px">
    <svg width="22" height="30" viewBox="0 0 22 30"><path d="M2 1v8c0 3 2 4 3 4v16h2V13c1 0 3-1 3-4V1H9v7H8V1H6v7H5V1H4v7H3V1z" fill="#111"/><path d="M14 29V1c4 1 6 6 6 13h-4v15z" fill="#111"/></svg>
    <h3>SUSPENDISSE VEL</h3>
    <p>Lorem ipsum dolor sit amet,<br>consectetur adipiscing elit.</p>
  </div>
  <div class="feature" style="left:334px">
    <svg width="36" height="30" viewBox="0 0 36 30"><path d="M14 2c-2 2 2 3 0 5M19 2c-2 2 2 3 0 5" fill="none" stroke="#111" stroke-width="1.5"/><path d="M4 11h24v5c0 6-5 10-12 10S4 22 4 16z" fill="#111"/><path d="M28 13h3a3 3 0 010 6h-4" fill="none" stroke="#111" stroke-width="2"/><rect x="1" y="27" width="32" height="2" fill="#111"/></svg>
    <h3>UT QUIS VELIT</h3>
    <p>Ut interdum tellus mi, in<br>condimentum odio convallis eu.</p>
  </div>
  <div class="feature" style="left:530px">
    <svg width="30" height="30" viewBox="0 0 30 30"><circle cx="15" cy="15" r="13" fill="#111"/><circle cx="15" cy="15" r="9" fill="none" stroke="#fff" stroke-width="1.2"/><path d="M15 6v18M6 15h18M9 9l12 12M21 9L9 21" stroke="#fff" stroke-width="1"/></svg>
    <h3>ALIQUAM ET!</h3>
    <p>Proin pellentesque arcu eu<br>elementum viverra.</p>
  </div>
  <div class="feature" style="left:718px">
    <svg width="30" height="30" viewBox="0 0 30 30"><path d="M18 6c2-3 5-4 8-3" fill="none" stroke="#111" stroke-width="2"/><g fill="#111"><circle cx="20" cy="9" r="3.5"/><circle cx="14" cy="9" r="3.5"/><circle cx="8" cy="11" r="3.5"/><circle cx="17" cy="14" r="3.5"/><circle cx="11" cy="16" r="3.5"/><circle cx="14" cy="21" r="3.5"/><circle cx="8" cy="22" r="3"/></g></svg>
    <h3>MAURIS EU MAURIS</h3>
    <p>In posuere elit non metus laoreet<br>sagittis. Etiam eu luctus.</p>
  </div>
</section>

<div class="city-map" role="img" aria-label="Yellow-toned street map of a city with a winding river"></div>
<form class="city-search">
  <span class="pin"><svg width="16" height="18" viewBox="0 0 16 18"><path d="M8 1a5 5 0 00-5 5c0 4 5 9 5 9s5-5 5-9a5 5 0 00-5-5z" fill="none" stroke="#444" stroke-width="1.5"/><circle cx="8" cy="6" r="1.8" fill="#444"/><path d="M1 17h14" stroke="#444" stroke-width="1.5"/></svg></span>
  <span class="label">Find Your City</span>
  <span class="go"><svg width="20" height="20" viewBox="0 0 20 20"><circle cx="8" cy="8" r="6" fill="none" stroke="#fff" stroke-width="2.2"/><path d="M12.5 12.5l6 6" stroke="#fff" stroke-width="2.6"/></svg></span>
</form>

<section class="testimonials">
  <h2>CLIENTS SPEAK</h2>
  <blockquote><span class="q">“</span>Lorem ipsum dolor sit amet, consectetur adipiscing elit. Ut interdum tellus mi, in condimentum odio convallis eu. Proin pellentesque arcu eu elementum viverra. In posuere elit non metus laoreet sagittis. Etiam eu nisi vehicula leo ornare luctus. Cras quis augue augue. Pellentesque sed placerat lacus. In molestie laoreet consectetur. In placerat mi a arcu molestie.<span class="q">”</span></blockquote>
  <p class="who">- Marla,</p>
  <p class="role">Managing Director ( Food Services Company )</p>
  <div class="slider-dots"><span></span><span class="on"></span><span></span></div>
</section>

<footer class="site-footer">
  <nav class="footer-nav">
    <a href="#">HOME</a><a href="#">CONTACT US</a><a href="#">ABOUT US</a><a href="#">HELP</a><a href="#">PRIVACY POLICY</a><a href="#">TERMS OF USE</a>
  </nav>
  <p class="copyright">Platerva © All right reserved.</p>
  <div class="social-links">
    <span style="background:#3b5fa8"></span><span style="background:#3aa2e0"></span><span style="background:#d8432e"></span><span style="background:#1c75b5"></span>
  </div>
</footer>

</body>
</html>
```